Car finance company business card

Create a nice business card for our car financing company , Visit our website www.birchlanefinance.com for the phone number and idea of the company look. Please do not be afraid to be creative. Name on card Is Marc-Antoine Beaulieu and phone number is on our website adress of business is
27816 Boulevard Saint-Orvel,
Mirabel, QC K4R 2T8

```html
<!DOCTYPE html>
<html lang="fr">
<head>
<meta charset="utf-8">
<title>Birch Lane Finance — Business Card</title>
<link href="https://fonts.googleapis.com/css2?family=Crimson+Text:wght@400;600&display=swap" rel="stylesheet">
<style>
  :root {
    --page-bg: #d9d6d2;
    --card-dark: #262626;
    --card-mid: #3e3e3e;
    --text-light: #ececec;
    --accent: #e8843a;
    --mascot-orange: #e9742c;
    --mascot-blue: #5a63b8;
  }
  * { box-sizing: border-box; margin: 0; padding: 0; }
  html, body {
    width: 1200px;
    height: 1200px;
    overflow: hidden;
    background: var(--page-bg);
  }
  body {
    display: flex;
    align-items: center;
    justify-content: center;
    font-family: "Crimson Text", Georgia, serif;
  }
  .card {
    position: relative;
    width: 1050px;
    height: 600px;
    border-radius: 6px;
    background: radial-gradient(ellipse at 55% 45%, var(--card-mid) 0%, var(--card-dark) 75%);
    box-shadow: 0 24px 50px rgba(0,0,0,0.35);
    overflow: hidden;
  }
  .brand {
    position: absolute;
    left: 62px;
    top: 130px;
    display: flex;
    align-items: center;
    gap: 14px;
    z-index: 2;
  }
  .brand-mark {
    width: 20px;
    height: 20px;
    border-radius: 50%;
    background: var(--text-light);
    flex: none;
  }
  .brand-name {
    font-size: 46px;
    font-weight: 600;
    color: var(--text-light);
    letter-spacing: 0.5px;
    line-height: 1;
    white-space: nowrap;
  }
  .contact {
    position: absolute;
    left: 66px;
    top: 290px;
    color: var(--text-light);
    z-index: 2;
  }
  .person-name {
    font-size: 32px;
    font-weight: 400;
    color: var(--accent);
    text-transform: uppercase;
    letter-spacing: 1px;
    line-height: 1.1;
    white-space: nowrap;
  }
  .person-role {
    font-size: 24px;
    line-height: 1.1;
    margin-bottom: 22px;
  }
  .address {
    font-size: 26px;
    line-height: 1.2;
    font-style: normal;
    margin-left: 16px;
    margin-bottom: 18px;
  }
  .links {
    list-style: none;
    font-size: 26px;
    line-height: 1.25;
  }
  .links li {
    display: flex;
    align-items: center;
    gap: 14px;
  }
  .links svg { width: 20px; height: 20px; flex: none; }
  .links .hl { color: var(--accent); }
  .mascot {
    position: absolute;
    right: 50px;
    top: 40px;
    width: 410px;
    height: 380px;
    border-radius: 40% 40% 30% 30%;
    background: linear-gradient(160deg, var(--mascot-orange) 0%, #d9582a 55%, var(--mascot-blue) 100%);
    opacity: 0.9;
    z-index: 1;
  }
</style>
</head>
<body>
  <section class="card">
    <div class="brand">
      <span class="brand-mark"></span>
      <span class="brand-name">Birch Lane Finance</span>
    </div>

    <div class="mascot" role="img" aria-label="Cartoon mascot character in a blue suit holding out car keys"></div>

    <div class="contact">
      <h1 class="person-name">Marc-Antoine Beaulieu</h1>
      <p class="person-role">manager</p>
      <address class="address">
        27816 Boulevard Saint-Orvel,<br>
        Mirabel, QC K4R 2T8
      </address>
      <ul class="links">
        <li>
          <svg viewBox="0 0 20 20" aria-hidden="true"><path fill="var(--accent)" d="M5 2l3 4-2 2c1 2 3 4 5 5l2-2 4 3-2 3C9 17 3 11 2 5z"/></svg>
          +(514) - 555 - 0192
        </li>
        <li>
          <svg viewBox="0 0 20 20" aria-hidden="true"><rect x="2" y="4" width="16" height="12" fill="var(--accent)"/><path d="M2 4l8 7 8-7" stroke="var(--card-dark)" stroke-width="1.5" fill="none"/></svg>
          info@birchlanefinance.com
        </li>
        <li>
          <svg viewBox="0 0 20 20" aria-hidden="true"><circle cx="10" cy="10" r="8" fill="none" stroke="var(--accent)" stroke-width="2"/><path d="M2 10h16M10 2c-4 4-4 12 0 16M10 2c4 4 4 12 0 16" stroke="var(--accent)" stroke-width="1.3" fill="none"/></svg>
          <span>www.<span class="hl">birchlanefinance</span>.com</span>
        </li>
      </ul>
    </div>
  </section>
</body>
</html>
```